Simple 1 page layout for quiet-harbor-tools.com

Visit http://quiet-harbor-tools.com

The site calculates ipv6 unique local addresses for free. The content will stay as it is. There's going to be Zorvix promoslots below the red box and at the bottom of the page.

The red box contains the most important information on this page. The users focus should go there immediately.

The contents below composition is also kind of important.

Reason: I'm very busy at the moment. I need more time for evaluation and feedback. Thanks for your contributions and your patience.

Target Market(s)

IT and networking people

Industry/Entity Type

Zorvix

Requirements
Must have
• I need all pieces nicely cut, so I only have to do HTML and CSS.

```html
<!DOCTYPE html>
<html lang="en">
<head>
<meta charset="utf-8">
<title>Quiet Harbor Tools – Local Network Address Generator</title>
<link rel="stylesheet" href="https://fonts.googleapis.com/css2?family=PT+Sans:wght@400;700&family=Arimo:wght@400;700&display=swap">
<style>
:root{
  --page-bg:#ececec;
  --header-bg:#151515;
  --header-line:#3a3a3a;
  --brand-green:#3fbf1f;
  --tagline:#b5b5b5;
  --panel-bg:#ffffff;
  --panel-border:#cfcfcf;
  --title-blue:#274d77;
  --text:#222222;
  --muted:#444444;
  --link:#2b62a6;
  --bullet:#b9b9b9;
  --button-top:#5bcc2a;
  --button-bottom:#3aa80f;
  --dash:#bdbdbd;
  --promo:#0a84c8;
}
*{box-sizing:border-box;margin:0;padding:0}
html,body{width:1200px;height:900px;overflow:hidden}
body{background:var(--page-bg);font-family:"Arimo",Arial,sans-serif;color:var(--text);position:relative}
.site-header{position:absolute;left:0;top:0;width:1200px;height:63px;background:var(--header-bg);box-shadow:0 1px 3px rgba(0,0,0,.35)}
.brand{position:absolute;left:173px;top:12px;font-family:"PT Sans",sans-serif;font-size:30px;font-weight:700;color:var(--brand-green);line-height:40px}
.header-divider{position:absolute;left:432px;top:16px;width:1px;height:30px;background:var(--header-line)}
.tagline{position:absolute;left:451px;top:21px;font-family:"PT Sans",sans-serif;font-size:16px;color:var(--tagline);letter-spacing:.3px}
.panel{position:absolute;background:var(--panel-bg);border:1px solid var(--panel-border);box-shadow:0 1px 3px rgba(0,0,0,.08)}
.result-panel{left:174px;top:103px;width:855px;height:139px}
.result-prefix{position:absolute;left:26px;top:16px;font-family:"PT Sans",sans-serif;font-size:26px;color:var(--title-blue)}
.subnet-row{position:absolute;left:26px;font-size:13px;font-weight:700;font-family:"PT Sans",sans-serif}
.subnet-row span{position:absolute;white-space:nowrap}
.subnet-row .sep{left:151px}
.subnet-row .val{left:181px}
.reload-button{position:absolute;left:469px;top:67px;width:368px;height:43px;border-radius:4px;background:linear-gradient(var(--button-top),var(--button-bottom));box-shadow:0 2px 2px rgba(0,0,0,.2);color:#fff;font-family:"PT Sans",sans-serif;font-size:17px;text-align:center;line-height:43px}
.content-panel{left:174px;top:274px;width:855px;height:700px}
.section-title{position:absolute;left:26px;font-family:"PT Sans",sans-serif;font-size:24px;font-weight:400;color:#1c1c1c}
.diagram{position:absolute;left:26px;top:61px;font-size:12.5px;line-height:21.5px;color:var(--muted);letter-spacing:.6px;white-space:pre}
.field-list{position:absolute;font-size:12px}
.field{position:absolute;white-space:nowrap}
.field b{position:absolute;left:0}
.field .sep{position:absolute}
.field .val{position:absolute;color:var(--muted)}
.dash-rule{position:absolute;left:26px;width:507px;border-top:1px dashed var(--dash)}
.intro{position:absolute;left:27px;top:380px;width:500px;font-size:11.5px;line-height:17px;color:var(--muted)}
.sub-heading{position:absolute;font-family:"PT Sans",sans-serif;font-size:14px;color:#1c1c1c}
.contents-box{position:absolute;left:569px;top:16px;width:268px;height:241px;border:1px solid var(--panel-border)}
.contents-box h2{position:absolute;left:17px;top:13px;font-family:"PT Sans",sans-serif;font-size:18px;font-weight:400}
.contents-box ul{position:absolute;left:22px;top:43px;list-style:none}
.contents-box li{position:relative;padding-left:14px;height:26.7px;font-size:13px;color:var(--link)}
.contents-box li::before{content:"";position:absolute;left:0;top:6px;width:6px;height:6px;border-radius:50%;background:var(--bullet)}
.promo-slot{position:absolute;left:569px;top:277px;width:268px;height:223px;background:var(--promo)}
</style>
</head>
<body>
<header class="site-header">
  <div class="brand">Quiet Harbor Tools</div>
  <div class="header-divider"></div>
  <div class="tagline">Local Network Address Generator</div>
</header>

<section class="panel result-panel">
  <div class="result-prefix">fd2d:52d3:7653::/48</div>
  <div class="subnet-row" style="top:67px"><span>1st 64-bit subnet</span><span class="sep">:</span><span class="val">fd2d:52d3:7653::/64</span></div>
  <div class="subnet-row" style="top:95px"><span>Last 64-bit subnet</span><span class="sep">:</span><span class="val">fd2d:52d3:7653:ffff::/64</span></div>
  <div class="reload-button">Just Reload This Page to Get a New One</div>
</section>

<main class="panel content-panel">
  <h1 class="section-title" style="top:16px">Composition</h1>
  <div class="diagram">| 7 bits |1| 40 bits | 16 bits | 64 bits |
+--------+-+------------+-----------+----------------------------+
| Prefix |L| Global ID | Subnet ID | Interface ID |
+--------+-+------------+-----------+----------------------------+</div>

  <div class="field-list" style="left:36px;top:171px">
    <div class="field" style="top:0"><b>Prefix</b><span class="sep" style="left:100px">:</span><span class="val" style="left:133px">fc::/7</span></div>
    <div class="field" style="top:28px"><b>Local (L)</b><span class="sep" style="left:100px">:</span><span class="val" style="left:133px">1</span></div>
    <div class="field" style="top:57px"><b>Global ID</b><span class="sep" style="left:100px">:</span><span class="val" style="left:133px">2d52d37653 changes every time you visit this page</span></div>
    <div class="field" style="top:85px"><b>Subnet ID</b><span class="sep" style="left:100px">:</span><span class="val" style="left:133px">0 - ffff use freely for your own IPv6 subnetting</span></div>
    <div class="field" style="top:114px"><b>Interface ID</b><span class="sep" style="left:100px">:</span><span class="val" style="left:134px">Your host address.</span></div>
  </div>

  <div class="dash-rule" style="top:326px"></div>
  <h2 class="section-title" style="top:341px">What's a Unique Local Address?</h2>
  <p class="intro">IPv6 unique local addresses are similar to the IPv4 private address classes with one big difference: THE ARE UNIQUE.</p>

  <div class="sub-heading" style="left:26px;top:432px">IPv4 private addresses</div>
  <div class="field-list" style="left:35px;top:471px">
    <div class="field" style="top:0"><b>Class A</b><span class="sep" style="left:80px">:</span><span class="val" style="left:110px">10.0.0.0/8</span></div>
    <div class="field" style="top:28px"><b>Class B</b><span class="sep" style="left:80px">:</span><span class="val" style="left:110px">172.16.0.0/12</span></div>
    <div class="field" style="top:57px"><b>Class C</b><span class="sep" style="left:80px">:</span><span class="val" style="left:110px">192.168.0.0/16</span></div>
  </div>
  <div class="sub-heading" style="left:26px;top:560px">IPv6 unique local addresses</div>
  <div class="field-list" style="left:221px;top:562px">
    <div class="field"><span class="sep" style="left:0">:</span><span class="val" style="left:23px">fd::/48 - fd:ffff:ffff::/48</span></div>
  </div>
  <div class="dash-rule" style="top:603px"></div>

  <nav class="contents-box">
    <h2>Contents</h2>
    <ul>
      <li>What's a unique local address?</li>
      <li>What's the use?</li>
      <li>Why do they need to be unique?</li>
      <li>Are they really globally unique?</li>
      <li>Isn't there an easy way?</li>
      <li>What is the subnet id?</li>
      <li>Where can I get more information?</li>
    </ul>
  </nav>
  <div class="promo-slot" role="img" aria-label="Promotional banner slot"></div>
</main>
</body>
</html>
```